Redesign of an insurance website

Attached is an insurance website that I need to redesign. Currently the website is too dark. I like for example www.brenvalo.com . Could you make the website lighter and change the structure a little so that it is more user friendly?

Industry/Entity Type

Insurance

Number of Pages Required

4 page

```html
<!DOCTYPE html>
<html lang="cs">
<head>
<meta charset="utf-8">
<title>Krytoplan.cz – srovnani pojisteni</title>
<link href="https://fonts.googleapis.com/css2?family=Raleway:wght@400;500;600;700&display=swap" rel="stylesheet">
<style>
:root{
  --blue:#2684fe;
  --orange:#f07a20;
  --ink:#333840;
  --panel:#f1f2f5;
  --footer:#d7dbe3;
  --line:#a9aeb8;
  --white:#ffffff;
}
*{box-sizing:border-box;margin:0;padding:0}
html,body{width:1200px;height:1200px;overflow:hidden}
body{font-family:'Raleway',sans-serif;color:var(--ink);background:var(--white);position:relative}
.abs{position:absolute}
.logo{font-weight:700;color:var(--blue);letter-spacing:.5px;white-space:nowrap}
.nav a{color:var(--orange);text-decoration:none;font-size:14px;position:absolute;white-space:nowrap;font-weight:500}
.btn{position:absolute;display:flex;align-items:center;justify-content:center;font-weight:700;font-size:12.5px;border-radius:3px;text-transform:uppercase}

.header{top:0;left:0;width:1200px;height:103px;background:var(--white);box-shadow:0 2px 8px rgba(0,0,0,.06);z-index:2}
.header .logo{left:61px;top:34px;font-size:30px}
.btn-login{left:849px;top:34px;width:134px;height:36px;border:2px solid var(--orange);color:var(--orange)}
.btn-register{left:1001px;top:34px;width:134px;height:36px;background:var(--blue);color:var(--white)}

.hero-left{top:103px;left:0;width:668px;height:489px;background:var(--white)}
.hero-right{top:103px;left:668px;width:532px;height:489px;background:var(--panel)}
.h2{font-weight:600;font-size:23px;white-space:nowrap}
.benefits{list-style:none;position:absolute;left:98px;top:217px}
.benefits li{display:flex;align-items:center;height:34px;font-size:14.5px}
.benefits svg{margin-right:12px;flex:none}

.field{position:absolute;border:1px solid #b6bac2;background:var(--white);font-size:13px;padding-left:12px;display:flex;align-items:center;border-radius:2px}
.btn-price{left:940px;top:355px;width:195px;height:36px;background:var(--blue);color:var(--white)}
.product{position:absolute;width:58px;height:58px;border-radius:50%;border:1.5px solid #8c9099;background:var(--white)}
.product.active{border:2px solid #222}

.promo{top:592px;left:0;width:1200px;height:447px;background:var(--blue);color:var(--white)}
.promo .h2{color:var(--white)}
.copy{position:absolute;font-size:14.5px;line-height:30.4px}
.divider{left:767px;top:23px;width:1px;height:402px;background:rgba(255,255,255,.35)}
.photo{left:424px;top:126px;width:303px;height:256px;background:linear-gradient(135deg,#e9e4d4 0%,#c9b98a 30%,#f3f4f2 55%,#dfe3ea 100%)}
.btn-save{left:63px;top:347px;width:134px;height:36px;border:2px solid var(--white);color:var(--white)}

.footer{top:1039px;left:0;width:1200px;height:161px;background:var(--footer)}
.footer .logo{left:63px;top:40px;font-size:23px}
.footer .nav a{top:48px;font-size:13px}
.newsletter-label{left:598px;top:48px;font-size:13px;font-weight:500;white-space:nowrap}
.btn-confirm{left:1036px;top:35px;width:99px;height:36px;background:var(--orange);color:var(--white)}
.rule{left:63px;top:105px;width:1072px;height:1px;background:var(--line)}
.legal{top:126px;left:0;width:1200px;display:flex;justify-content:center;gap:32px;font-size:10.5px;font-weight:500}
</style>
</head>
<body>

<header class="header abs">
  <div class="logo abs">KRYTOPLAN.CZ</div>
  <nav class="nav">
    <a style="left:320px;top:46px">O NAS</a>
    <a style="left:389px;top:46px">CASTÉ DOTAZY</a>
    <a style="left:520px;top:46px">KONTAKT</a>
  </nav>
  <div class="btn btn-login">Prihlasit se</div>
  <div class="btn btn-register">Regitsrovat</div>
</header>

<section class="hero-left abs">
  <h2 class="h2 abs" style="left:102px;top:58px">Proc hledat pojisteni pres Krytoplan.cz?</h2>
</section>
<ul class="benefits">
  <li><svg width="21" height="21" viewBox="0 0 21 21"><circle cx="10.5" cy="10.5" r="10.5" fill="#f07a20"/><path d="M6 10.8l3 3 6-6.2" stroke="#fff" stroke-width="2.2" fill="none"/></svg>S nami najdete tu nejvyhodnejsi nabidku</li>
  <li><svg width="21" height="21" viewBox="0 0 21 21"><circle cx="10.5" cy="10.5" r="10.5" fill="#f07a20"/><path d="M6 10.8l3 3 6-6.2" stroke="#fff" stroke-width="2.2" fill="none"/></svg>Zarucime vam nejlepsi cenu na trhu</li>
  <li><svg width="21" height="21" viewBox="0 0 21 21"><circle cx="10.5" cy="10.5" r="10.5" fill="#f07a20"/><path d="M6 10.8l3 3 6-6.2" stroke="#fff" stroke-width="2.2" fill="none"/></svg>Staci par minut a muzete usetrit tisice</li>
  <li><svg width="21" height="21" viewBox="0 0 21 21"><circle cx="10.5" cy="10.5" r="10.5" fill="#f07a20"/><path d="M6 10.8l3 3 6-6.2" stroke="#fff" stroke-width="2.2" fill="none"/></svg>Srovnavame vsechny pojistovny</li>
  <li><svg width="21" height="21" viewBox="0 0 21 21"><circle cx="10.5" cy="10.5" r="10.5" fill="#f07a20"/><path d="M6 10.8l3 3 6-6.2" stroke="#fff" stroke-width="2.2" fill="none"/></svg>Zaridime vam vsechny pojistovny</li>
  <li><svg width="21" height="21" viewBox="0 0 21 21"><circle cx="10.5" cy="10.5" r="10.5" fill="#f07a20"/><path d="M6 10.8l3 3 6-6.2" stroke="#fff" stroke-width="2.2" fill="none"/></svg>Vse vyridite z pohodli domova</li>
  <li><svg width="21" height="21" viewBox="0 0 21 21"><circle cx="10.5" cy="10.5" r="10.5" fill="#f07a20"/><path d="M6 10.8l3 3 6-6.2" stroke="#fff" stroke-width="2.2" fill="none"/></svg>Nemusite nikam chodit a usetrite</li>
</ul>

<section class="hero-right abs">
  <h2 class="h2 abs" style="left:0;width:532px;text-align:center;top:58px">Najdete nejvyhodnejsi pojisteni</h2>
  <div class="abs" role="img" aria-label="Ikona pojisteni auta – klice" style="left:226px;top:106px;width:82px;height:82px;border-radius:50%;background:var(--blue)"></div>
</section>

<div class="field" style="left:736px;top:310px;width:195px;height:36px">Jmeno</div>
<div class="field" style="left:940px;top:310px;width:195px;height:36px">E-mail</div>
<div class="field" style="left:736px;top:355px;width:195px;height:36px">Prijmeni</div>
<div class="btn btn-price">Spocitat cenu</div>

<h3 class="h2 abs" style="left:668px;width:532px;text-align:center;top:421px;font-size:19.5px">Chcete pojistit neco jineho?</h3>
<svg class="abs" style="left:736px;top:487px" width="12" height="20" viewBox="0 0 12 20"><path d="M10 2L2 10l8 8" stroke="#333" stroke-width="1.6" fill="none"/></svg>
<svg class="abs" style="left:1124px;top:487px" width="12" height="20" viewBox="0 0 12 20"><path d="M2 2l8 8-8 8" stroke="#333" stroke-width="1.6" fill="none"/></svg>
<div class="product active" role="img" aria-label="Pojisteni auta" style="left:775px;top:467px"></div>
<div class="product" role="img" aria-label="Pojisteni cestovni – karavan" style="left:841px;top:467px"></div>
<div class="product" role="img" aria-label="Pojisteni kola" style="left:906px;top:467px"></div>
<div class="product" role="img" aria-label="Pojisteni majetku – penezenka" style="left:973px;top:467px"></div>
<div class="product" role="img" aria-label="Cestovni pojisteni – letadlo" style="left:1038px;top:467px"></div>

<section class="promo abs">
  <h2 class="h2 abs" style="left:62px;top:62px">Uzavreli jste v minulosti nevyhodnou pojistku? Zbavte se ji!</h2>
  <p class="copy" style="left:63px;top:117px;width:335px">Lorem ipsum dolor sit amet, consectetur adipis cing elit. Sed enim augue, fringilla vel felis a, blandit maximus lorem. Vestibulum ante ipsum primis in faucibus orci luctus et ultrices posuere cubilia Curae; Donec quis aliquet eros, quis mi. Integer suscipit lacinia mauris, a lacinia lorem scelerisque commodo. Vivamus tempor.</p>
  <div class="photo abs" role="img" aria-label="Fotografie zlateho budiku zblizka"></div>
  <div class="btn btn-save">Chci usetrit</div>
  <div class="divider abs"></div>
  <h2 class="h2 abs" style="left:803px;top:62px">Jak to funguje</h2>
  <p class="copy" style="left:803px;top:117px;width:335px">Lorem ipsum dolor sit amet, consectetur adipis cing elit. Sed enim augue, fringilla vel felis a, blandit maximus lorem. Vestibulum ante ipsum primis in faucibus orci luctus et ultrices posuere cubilia Curae; Donec quis aliquet eros, quis mi. Integer suscipit lacinia mauris, a lacinia lorem scelerisque commodo. Vivamus tempor. lacinia lorem scelerisque commodo. Vivamus tempor.</p>
</section>

<footer class="footer abs">
  <div class="logo abs">KRYTOPLAN.CZ</div>
  <nav class="nav">
    <a style="left:259px">O NAS</a>
    <a style="left:319px">CASTÉ DOTAZY</a>
    <a style="left:434px">KONTAKT</a>
  </nav>
  <div class="newsletter-label abs">ODEBRAT NEWSLETTER</div>
  <div class="field" style="left:760px;top:35px;width:268px;height:36px">E-mail</div>
  <div class="btn btn-confirm">Potvrdit</div>
  <div class="rule abs"></div>
  <div class="legal abs">
    <span>Ochrana soukromi</span>
    <span>Podminky poulziti</span>
    <span>Copyright 2017 Krytoplan.cz Vsechna prava vyhrazena.</span>
  </div>
</footer>

</body>
</html>
```